Electrical Contracting business website design

Website needed to help promote an online footprint focused on local customers in my area Gympie, QLD,Australia 4570

I am after a clear website (one where my customer does not get lost or frustrated)
most important is to engage customer to Call now or Request a quote with all the lead details.

Some bread and butter work for us is broken hot water units, electrical faults and renovators

We offer all sorts of services
- smoke alarms
- Test n Tag
- Lighting
- Fans
- A/C
- Design and planning
- safety switches
- underground Power
- Energy efficient solutions
- hot water repair
- Fault finding
- Control / Automation

Target Market(s)

Local Customers, Renovators, Builders, Commercial, Industrial, Domestic

Industry/Entity Type

Electrician

Coding

Coded - Design and coding required

Number of Pages Required

1 page

Colors
f78f20
000000
ec1f27
ffffff

Requirements
Must have
• Easy to use website with clear Contact Information (call now button)
• Ph: 0491527308 24/7
• Email Brightvoltservices@examplemail.com
• , Quote request to receive leads and customer info

```html
<!DOCTYPE html>
<html lang="en">
<head>
<meta charset="utf-8">
<title>Brightvolt Services – Local and Trusted Electrical Experts</title>
<link href="https://fonts.googleapis.com/css2?family=Rubik:wght@500;700;800&family=Lato:wght@400;700&display=swap" rel="stylesheet">
<style>
:root{
  --orange:#f78f20;
  --red:#ec1f27;
  --black:#000000;
  --white:#ffffff;
  --header:#1e1b1b;
  --ink:#222222;
  --text:#3a3a3a;
  --muted:#8a8a8a;
  --line:#d6d2d2;
  --service-bg:#f4f1f1;
  --why-bg:#ececec;
  --footer:#0d0d0d;
  --head-font:'Rubik',sans-serif;
  --body-font:'Lato',sans-serif;
}
*{box-sizing:border-box;margin:0;padding:0}
html,body{width:1200px;height:4071px;overflow:hidden}
body{font-family:var(--body-font);color:var(--text);background:var(--white);position:relative}
section,header,footer{position:relative;width:1200px;overflow:hidden}
.abs{position:absolute}
.brand{display:flex;align-items:center;gap:10px;font-family:var(--head-font);font-weight:700;color:var(--orange);font-size:25px;line-height:1.05;letter-spacing:.5px}
.brand-mark{width:22px;height:22px;background:var(--orange);flex:none}
.section-title{position:absolute;left:0;width:1200px;text-align:center;font-family:var(--head-font);font-weight:800;font-size:28px;color:var(--ink);letter-spacing:.2px}
.title-rule{position:absolute;left:572px;width:57px;height:4px;background:#a9a9a9}

/* header */
.site-header{height:120px;background:var(--header)}
.site-header .brand{left:131px;top:32px;position:absolute;width:230px}
.contact-chip{position:absolute;display:flex;align-items:center;gap:14px;color:var(--white)}
.contact-chip small{display:block;font-size:13px;line-height:16px}
.contact-chip strong{display:block;font-size:14.5px;font-weight:400}
.contact-chip .big{font-family:var(--head-font);font-weight:700;font-size:26px;line-height:28px}
.main-nav{position:absolute;top:87px;left:454px;display:flex;gap:0}
.main-nav a{font-family:var(--head-font);font-weight:700;font-size:12.5px;color:var(--white);text-decoration:none;letter-spacing:.3px;margin-right:32px}
.main-nav a.active{color:var(--orange);text-decoration:underline;text-underline-offset:4px}

/* hero */
.hero{height:517px;background:linear-gradient(100deg,#4a4a4a 0%,#8a8584 22%,#b9b3ae 38%,#a3584c 50%,#c9c0b8 62%,#7b7572 80%,#5a5553 100%)}
.quote-box{position:absolute;left:751px;top:48px;width:318px;height:393px;background:rgba(247,245,244,.97);padding:22px 22px}
.quote-box h2{font-family:var(--head-font);font-weight:500;font-size:23px;line-height:30px;color:#333}
.field{position:absolute;left:25px;width:271px;height:36px;border:1px solid #bdbdbd;background:var(--white);font-size:11.5px;color:#555;padding:10px 12px}
.submit{position:absolute;left:25px;top:322px;width:271px;height:48px;background:var(--orange);color:var(--white);font-family:var(--head-font);font-weight:700;font-size:19px;display:flex;align-items:center;justify-content:center;letter-spacing:.5px}
.dots{position:absolute;left:549px;top:450px;display:flex;gap:14px;align-items:center}
.dots i{width:9px;height:9px;border-radius:50%;background:var(--white);display:block}
.dots i.on{width:14px;height:14px;background:var(--orange);border:2px solid var(--white)}

/* services */
.services{height:781px;background:var(--service-bg)}
.service-grid{position:absolute;left:128px;top:134px;display:grid;grid-template-columns:133px 177px 207px 145px 121px 158px;grid-template-rows:132px 132px}
.service{display:flex;flex-direction:column;align-items:center;justify-content:flex-start;padding-top:22px;border-right:1px solid var(--line);font-size:14.5px;color:#2d2d2d}
.service:nth-child(6n){border-right:none}
.service:nth-child(-n+6){border-bottom:1px solid var(--line)}
.service svg{width:48px;height:48px;margin-bottom:14px}
.truck{position:absolute;left:206px;top:454px;width:782px;height:310px;border-radius:40px 60px 20px 20px;background:linear-gradient(180deg,#2b2b2b 0%,#0f0f0f 60%,#1a1a1a 100%)}
.truck-shadow{position:absolute;left:150px;top:740px;width:900px;height:60px;border-radius:50%;background:radial-gradient(ellipse at center,rgba(0,0,0,.35),rgba(0,0,0,0) 70%)}

/* welcome */
.welcome{height:683px;background:var(--white)}
.team-photo{position:absolute;left:131px;top:98px;width:494px;height:525px;background:linear-gradient(160deg,#7d8a6c 0%,#9c958a 40%,#5d6b86 70%,#3f4f6e 100%)}
.welcome .kicker{position:absolute;left:677px;top:150px;font-family:var(--head-font);font-weight:700;font-size:19px;color:var(--ink)}
.welcome h2{position:absolute;left:677px;top:178px;font-family:var(--head-font);font-weight:800;font-size:29px;color:var(--ink)}
.welcome .rule{position:absolute;left:677px;top:232px;width:40px;height:4px;background:#a9a9a9}
.welcome p{position:absolute;left:677px;top:276px;width:400px;font-size:15.6px;line-height:24px;color:#3a3a3a}
.btn{display:flex;align-items:center;justify-content:center;background:var(--orange);color:var(--white);font-family:var(--head-font);font-weight:700}
.welcome .btn{position:absolute;left:677px;top:531px;width:117px;height:40px;font-size:13px}

/* why */
.why{height:602px;background:linear-gradient(115deg,#e9e9e9 0%,#f3f3f3 18%,#e6e6e6 30%,#f2f2f2 48%,#e7e7e7 62%,#f1f1f1 80%,#e8e8e8 100%)}
.perk{position:absolute;display:flex;align-items:center;gap:22px;font-size:14.5px;line-height:19px;color:#2a2a2a}
.perk .ring{width:74px;height:74px;border-radius:50%;border:3px solid #7a7a7a;background:var(--white);display:flex;align-items:center;justify-content:center;flex:none}
.perk .ring svg{width:34px;height:34px}
.center-brand{position:absolute;left:470px;top:170px;width:260px;display:flex;flex-direction:column;align-items:center;gap:18px}
.center-brand .disc{width:170px;height:170px;border-radius:50%;background:var(--orange)}
.center-brand span{font-family:var(--head-font);font-weight:800;font-size:40px;color:var(--orange)}

/* testimonials */
.testimonials{height:580px;background:var(--white)}
.card{position:absolute;top:222px;width:459px;height:232px;border:1.5px solid #cfcfcf;background:var(--white);padding:68px 50px 0;text-align:center;font-size:14.6px;line-height:22.5px;color:#333}
.card::after{content:"";position:absolute;left:50%;bottom:-12px;width:20px;height:20px;background:var(--white);border-right:1.5px solid #cfcfcf;border-bottom:1.5px solid #cfcfcf;transform:translateX(-50%) rotate(45deg)}
.avatar{position:absolute;top:181px;width:82px;height:82px;border-radius:50%;border:3px solid var(--orange);background:linear-gradient(180deg,#a9b6c4,#4f5b6b)}
.reviewer{position:absolute;top:491px;width:459px;text-align:center;font-size:12px;color:#333}
.reviewer b{font-weight:700}
.arrow{position:absolute;top:314px;width:38px;height:38px;border-radius:50%;border:1.5px solid #a0a0a0;display:flex;align-items:center;justify-content:center}

/* tradition */
.tradition{height:374px;background:linear-gradient(180deg,#262626 0%,#2f2e2d 45%,#1f1f1f 100%)}
.tradition h2{position:absolute;left:0;top:74px;width:1200px;text-align:center;font-family:var(--head-font);font-weight:800;font-size:28px;color:var(--white)}
.tradition p{position:absolute;left:320px;top:140px;width:560px;text-align:center;font-size:19px;line-height:28px;color:#e0e0e0}
.tradition .btn{position:absolute;left:504px;top:262px;width:190px;height:56px;font-size:19px}

/* footer */
.site-footer{height:414px;background:var(--footer);color:#ddd}
.site-footer .brand{position:absolute;left:131px;top:134px;width:230px}
.foot-head{position:absolute;top:64px;font-family:var(--head-font);font-weight:700;font-size:14px;color:var(--white);letter-spacing:.3px}
.foot-menu{position:absolute;left:419px;top:110px;list-style:none;font-size:13.5px;line-height:24px;color:#e6e6e6}
.foot-item{position:absolute;display:flex;gap:12px;align-items:flex-start;font-size:13.5px;line-height:19px;color:#e6e6e6}
.foot-item .dot{width:26px;height:26px;border-radius:50%;background:var(--white);display:flex;align-items:center;justify-content:center;flex:none;margin-top:2px}
.foot-rule{position:absolute;left:111px;top:336px;width:980px;height:1px;background:#333}
.copyright{position:absolute;left:0;top:363px;width:1200px;text-align:center;font-size:11.5px;color:#cfcfcf}
</style>
</head>
<body>

<header class="site-header">
  <div class="brand"><span class="brand-mark"></span>Brightvolt Services</div>
  <div class="contact-chip" style="left:562px;top:24px">
    <svg width="30" height="22" viewBox="0 0 30 22"><rect x="1" y="1" width="28" height="20" rx="2" fill="#fff"/><path d="M2 3l13 10 13-10" fill="none" stroke="#1e1b1b" stroke-width="2.2"/></svg>
    <div><small>E mail us</small><strong>Brightvoltservices@examplemail.com</strong></div>
  </div>
  <div class="contact-chip" style="left:864px;top:20px">
    <svg width="36" height="36" viewBox="0 0 36 36"><path d="M9 5c2-1 3 0 4 2l2 4c1 2 0 3-1 4l-1 1c1 3 4 6 7 7l1-1c1-1 2-2 4-1l4 2c2 1 3 2 2 4-1 3-4 5-7 4C15 29 7 21 5 12 4 9 6 6 9 5z" fill="#fff"/><text x="18" y="17" font-family="Rubik,sans-serif" font-size="10" font-weight="700" fill="#fff">24</text></svg>
    <div><small>CALL US 24/7</small><span class="big">0491527308</span></div>
  </div>
  <nav class="main-nav">
    <a class="active">HOME</a><a>ABOUT US</a><a>SERVICES</a><a>PROJECTS</a><a>TESTIMONIALS</a><a style="margin-right:0">CONTACT US</a>
  </nav>
</header>

<section class="hero">
  <div class="abs" role="img" aria-label="Electrician in work gloves wiring a switchboard with red and coloured cables" style="left:0;top:0;width:1200px;height:517px"></div>
  <form class="quote-box">
    <h2>LOCAL AND TRUSTED<br>ELECTRICAL EXPERTS</h2>
    <div class="field" style="top:96px">Name</div>
    <div class="field" style="top:139px">Phone</div>
    <div class="field" style="top:183px">E mail</div>
    <div class="field" style="top:227px;height:82px">Message</div>
    <div class="submit">SUBMIT</div>
  </form>
  <div class="dots"><i></i><i></i><i class="on"></i><i></i><i></i></div>
</section>

<section class="services">
  <h2 class="section-title" style="top:42px">OUR SERVICES</h2>
  <div class="title-rule" style="top:88px"></div>
  <div class="service-grid">
    <div class="service"><svg viewBox="0 0 48 48" fill="none" stroke="#333" stroke-width="2.5"><path d="M4 12h40M10 18h28M16 24h16"/><path d="M24 4v8M18 30l-3 6M30 30l3 6M24 30v8"/></svg>Smoke Alarms</div>
    <div class="service"><svg viewBox="0 0 48 48" fill="none" stroke="#333" stroke-width="3.5" stroke-linecap="round"><path d="M10 10l28 28M38 10L10 38"/><circle cx="10" cy="10" r="5" stroke-width="2.5"/></svg>Test n Tag</div>
    <div class="service"><svg viewBox="0 0 48 48"><path d="M24 4a14 14 0 0 0-8 25v7h16v-7a14 14 0 0 0-8-25z" fill="#333"/><rect x="17" y="38" width="14" height="3" fill="#333"/><rect x="19" y="43" width="10" height="3" fill="#333"/></svg>Lighting</div>
    <div class="service"><svg viewBox="0 0 48 48" fill="#333"><circle cx="24" cy="24" r="4"/><path d="M22 20L4 20c-2 2-2 6 0 7l18-1zM26 20l18 0c2 2 2 6 0 7l-18-1zM22 28l-2 16h8l-2-16z"/></svg>Fans</div>
    <div class="service"><svg viewBox="0 0 48 48" fill="none" stroke="#333" stroke-width="2.5"><rect x="4" y="8" width="40" height="16" rx="2" fill="#333"/><path d="M10 28v6M18 28c0 6 4 6 4 12M26 28c0 6-4 6-4 12M36 28v6"/></svg>A/C</div>
    <div class="service"><svg viewBox="0 0 48 48" fill="#333"><path d="M6 36L36 6l6 6-30 30z"/><path d="M8 8l6-2 30 30-4 6-30-30z" opacity=".8"/></svg>Design and planning</div>
    <div class="service"><svg viewBox="0 0 48 48" fill="none" stroke="#333" stroke-width="2.5"><rect x="14" y="4" width="20" height="40" rx="2"/><rect x="20" y="12" width="8" height="16" fill="#333"/></svg>Safety Switches</div>
    <div class="service"><svg viewBox="0 0 48 48" fill="#333"><rect x="16" y="14" width="16" height="14" rx="2"/><path d="M20 6v8M28 6v8" stroke="#333" stroke-width="3"/><path d="M22 28h4v8h-4zM24 36v10" stroke="#333" stroke-width="3"/></svg>Underground Power</div>
    <div class="service"><svg viewBox="0 0 48 48" fill="none" stroke="#333" stroke-width="3"><path d="M4 30c6-4 10 4 16 0s10 4 16 0 6 0 8 0M4 38c6-4 10 4 16 0s10 4 16 0 6 0 8 0"/><path d="M26 4l-8 14h8l-4 10" stroke-width="2.5"/></svg>Energy efficient solutions</div>
    <div class="service"><svg viewBox="0 0 48 48" fill="#333"><rect x="14" y="4" width="20" height="32" rx="3"/><circle cx="24" cy="16" r="3" fill="#f4f1f1"/><path d="M18 36v8M30 36v8" stroke="#333" stroke-width="3"/></svg>Hot water repair</div>
    <div class="service"><svg viewBox="0 0 48 48" fill="none" stroke="#333" stroke-width="4"><circle cx="19" cy="19" r="13"/><path d="M29 29l14 14" stroke-linecap="round"/></svg>Fault finding</div>
    <div class="service"><svg viewBox="0 0 48 48"><path d="M24 2l4 6 7-2 1 7 7 2-3 7 4 6-6 4 1 7-7 0-3 7-5-5-5 5-3-7-7 0 1-7-6-4 4-6-3-7 7-2 1-7 7 2z" fill="#333"/><circle cx="24" cy="24" r="7" fill="#f4f1f1"/></svg>Control / Automation</div>
  </div>
  <div class="truck-shadow"></div>
  <div class="truck" role="img" aria-label="Black service utility truck with branded tool canopy"></div>
</section>

<section class="welcome">
  <div class="team-photo" role="img" aria-label="Two electricians in work uniforms and hats standing outdoors"></div>
  <div class="kicker">WELCOME TO</div>
  <h2>BRIGHTVOLT SERVICES</h2>
  <div class="rule"></div>
  <p>Lorem ipsum dolor sit amet, consectetur adipiscing elit, sed do eiusmod tempor incididunt ut labore et dolore magna aliqua. Ut enim ad minim veniam, quis nostrud exercitation ullamco laboris nisi ut aliquip ex ea commodo consequat. Duis aute irure dolor in reprehenderit in voluptate velit esse cillum dolore eu fugiat nulla pariatur. Excepteur sint occaecat cupidatat non proident, sunt in cul pa qui officia deserunt mollit.</p>
  <div class="btn">READ MORE</div>
</section>

<section class="why">
  <h2 class="section-title" style="top:50px">WHY CHOOSE US</h2>
  <div class="title-rule" style="top:106px"></div>

  <div class="perk" style="left:134px;top:159px"><div class="ring"><svg viewBox="0 0 34 34" fill="none" stroke="#f78f20" stroke-width="2"><rect x="2" y="10" width="18" height="12"/><path d="M20 13h6l5 5v4H20"/><circle cx="9" cy="25" r="3"/><circle cx="26" cy="25" r="3"/></svg></div>Same Day Service</div>
  <div class="perk" style="left:134px;top:262px"><div class="ring"><svg viewBox="0 0 34 34" fill="none" stroke="#f78f20" stroke-width="2"><path d="M8 4c2-1 3 0 4 2l2 3c0 2-1 3-2 3 1 3 4 6 7 7 0-1 1-2 3-2l3 2c2 1 2 3 1 4-1 3-4 4-7 3C12 24 6 18 5 11c0-3 1-6 3-7z"/><text x="17" y="15" font-size="9" fill="#f78f20" stroke="none" font-family="Rubik,sans-serif" font-weight="700">24</text></svg></div>Emergency&nbsp; Services<br>Available</div>
  <div class="perk" style="left:134px;top:371px"><div class="ring"><svg viewBox="0 0 34 34" fill="none" stroke="#f78f20" stroke-width="2"><rect x="7" y="3" width="20" height="28" rx="2"/><path d="M11 10h12M11 15h12M11 20h7"/><circle cx="22" cy="25" r="3"/></svg></div>Licensed, Bonded,<br>and Insured</div>
  <div class="perk" style="left:134px;top:478px"><div class="ring"><svg viewBox="0 0 34 34" fill="none" stroke="#f78f20" stroke-width="2.5" stroke-linecap="round"><path d="M6 6l22 22M28 6L6 28"/></svg></div>Over 10 Years of<br>Experience</div>

  <div class="perk" style="left:827px;top:159px">100% Satisfaction<br>Guaranteed<div class="ring" style="margin-left:44px"><svg viewBox="0 0 34 34" fill="none" stroke="#f78f20" stroke-width="2"><path d="M4 15h6v15H4zM10 16l6-10c2 0 3 2 2 5l-1 4h10c2 0 3 2 2 4l-3 9c-1 2-2 2-4 2H10"/></svg></div></div>
  <div class="perk" style="left:827px;top:262px">Upfront Pricing –<br>No Hidden Fees<div class="ring" style="margin-left:63px"><svg viewBox="0 0 34 34" fill="none" stroke="#f78f20" stroke-width="3"><circle cx="17" cy="17" r="13"/><path d="M8 26L26 8"/></svg></div></div>
  <div class="perk" style="left:827px;top:371px">We Offer 15%<br>Off Any Job<div class="ring" style="margin-left:92px"><svg viewBox="0 0 34 34" fill="none" stroke="#f78f20" stroke-width="2"><rect x="4" y="12" width="26" height="6"/><rect x="6" y="18" width="22" height="12"/><path d="M17 12v18M17 12c-3-6-9-6-8-2s8 2 8 2c3-6 9-6 8-2s-8 2-8 2"/></svg></div></div>
  <div class="perk" style="left:827px;top:478px">Get Support<div class="ring" style="margin-left:103px"><svg viewBox="0 0 34 34" fill="none" stroke="#f78f20" stroke-width="2.2"><path d="M6 20v-4a11 11 0 0 1 22 0v4"/><rect x="4" y="18" width="5" height="8" rx="2"/><rect x="25" y="18" width="5" height="8" rx="2"/><path d="M27 26c0 3-3 4-8 4"/></svg></div></div>

  <div class="center-brand"><div class="disc"></div><span>BRIGHTVOLT</span></div>
</section>

<section class="testimonials">
  <h2 class="section-title" style="top:60px">TESTIMONIALS</h2>
  <div class="title-rule" style="top:116px"></div>
  <div class="arrow" style="left:57px"><svg width="12" height="14" viewBox="0 0 12 14"><path d="M9 1L3 7l6 6" fill="none" stroke="#888" stroke-width="1.6"/></svg></div>
  <div class="arrow" style="left:1099px"><svg width="12" height="14" viewBox="0 0 12 14"><path d="M3 1l6 6-6 6" fill="none" stroke="#888" stroke-width="1.6"/></svg></div>

  <div class="card" style="left:131px">“Lorem ipsum dolor sit amet, conse ctetur adipiscing elit, sed do eiusmod tempor incid idunt ut labore et dolore magna aliqua. Ut enim ad minim veni am, quis nostrud exercitation ulla mco laboris nisi ut aliquip ex ea com modo consequat. Duis aute irure dolor ”</div>
  <div class="card" style="left:609px">“Lorem ipsum dolor sit amet, conse ctetur adipiscing elit, sed do eiusmod tempor incid idunt ut labore et dolore magna aliqua. Ut enim ad minim veni am, quis nostrud exercitation ulla mco laboris nisi ut aliquip ex ea com modo consequat. Duis aute irure dolor ”</div>
  <div class="avatar" style="left:319px" role="img" aria-label="Customer portrait"></div>
  <div class="avatar" style="left:797px" role="img" aria-label="Customer portrait"></div>
  <div class="reviewer" style="left:131px"><b>DANIEL</b>,Australia</div>
  <div class="reviewer" style="left:609px"><b>DANIEL</b>,Australia</div>
</section>

<section class="tradition">
  <div class="abs" role="img" aria-label="Dimly lit workshop interior behind a dark overlay" style="left:0;top:0;width:1200px;height:374px"></div>
  <h2>A TRADITION OF QUALITY</h2>
  <p>Lorem ipsum dolor sit amet, conse ctetur adipiscing elit, sed do eiusmod tempor incid idunt ut labore et dolore magna aliqua. Ut enim ad minim veni am, quis nostrud exercitation.</p>
  <div class="btn">CONTACT US</div>
</section>

<footer class="site-footer">
  <div class="brand"><span class="brand-mark"></span>Brightvolt Services</div>

  <div class="foot-head" style="left:419px">MENU</div>
  <ul class="foot-menu"><li>HOME</li><li>ABOUT US</li><li>SERVICES</li><li>PROJECTS</li><li>TESTIMONIALS</li><li>CONTACT US</li></ul>

  <div class="foot-head" style="left:628px">CONTACT US</div>
  <div class="foot-item" style="left:627px;top:111px"><span class="dot"><svg width="12" height="14" viewBox="0 0 12 14"><path d="M6 0a5 5 0 0 0-5 5c0 4 5 9 5 9s5-5 5-9a5 5 0 0 0-5-5z" fill="#0d0d0d"/><circle cx="6" cy="5" r="2" fill="#fff"/></svg></span><span>48 Ridgeway Lane<br>Gympie, QLD 4570</span></div>
  <div class="foot-item" style="left:627px;top:173px"><span class="dot"><svg width="12" height="12" viewBox="0 0 12 12"><path d="M3 0c1 0 1 1 2 2l-1 2c1 2 2 3 4 4l2-1c1 1 2 1 2 2l-1 2C6 11 1 6 1 1z" fill="#0d0d0d"/></svg></span><span>Call Us<br>&nbsp;0491527308</span></div>
  <div class="foot-item" style="left:627px;top:235px"><span class="dot"><svg width="12" height="10" viewBox="0 0 12 10"><rect x="0" y="0" width="12" height="10" rx="1" fill="#0d0d0d"/><path d="M1 1l5 4 5-4" fill="none" stroke="#fff" stroke-width="1.2"/></svg></span><span>E mail Us<br>Brightvoltservices@examplemail.com</span></div>

  <div class="foot-head" style="left:939px">FOLLOW US</div>
  <div class="foot-item" style="left:939px;top:111px"><span class="dot"></span><span>Like us on<br>COMMUNITY PAGE</span></div>
  <div class="foot-item" style="left:939px;top:172px"><span class="dot"></span><span>Follow us on<br>NEWS FEED</span></div>
  <div class="foot-item" style="left:939px;top:234px"><span class="dot"></span><span>Follow us on<br>BUSINESS NETWORK</span></div>

  <div class="foot-rule"></div>
  <div class="copyright">Copyright © 2019 All Rights Reserved</div>
</footer>

</body>
</html>
```